Bao Lotus Menu Design Project

This project is pretty straight forward. You will be given 3 files which include the following:
1. Our proposed menu
2. Our Company logo
3. A sample menu on what we are looking for design wise

Your job is to create a visually pleasing menu that is simple, clean and fresh. Please refer to our home website for additional information. (www.baolotus-example.com) Must be in eps or equivalent format.

Target Market(s)

20s to 40s

Industry/Entity Type

It Company

Requirements
Must have
• Company log
Must be in EPS format

```html
<!DOCTYPE html>
<html lang="en">
<head>
<meta charset="utf-8">
<title>Bao Lotus — Beef &amp; Pork / Seafood Menu</title>
<link href="https://fonts.googleapis.com/css2?family=Josefin+Sans:ital,wght@0,400;0,600;0,700;1,300;1,400;1,600&display=swap" rel="stylesheet">
<style>
  :root {
    --ink: #050303;
    --text: #ffffff;
    --accent-red: #c9262b;
    --divider: #b0201f;
    --gold: #c9a23a;
    --ember: #7a2216;
  }
  html, body {
    margin: 0;
    padding: 0;
    overflow: hidden;
    background: var(--ink);
  }
  .menu-page {
    position: relative;
    width: 1200px;
    height: 1000px;
    overflow: hidden;
    background: var(--ink);
    font-family: "Josefin Sans", sans-serif;
    color: var(--text);
  }
  .backdrop-pattern {
    position: absolute;
    inset: 0;
    background:
      radial-gradient(ellipse 60% 45% at 50% 50%, rgba(5,3,3,0.95), rgba(5,3,3,0.55) 70%, rgba(5,3,3,0) 100%),
      linear-gradient(180deg, rgba(201,162,58,0.35) 0%, rgba(90,60,20,0.18) 35%, rgba(60,20,10,0.15) 60%, rgba(160,45,35,0.45) 100%);
  }
  .column-divider {
    position: absolute;
    left: 600px;
    top: 47px;
    width: 3px;
    height: 898px;
    background: var(--divider);
  }
  .menu-section {
    position: absolute;
    top: 52px;
  }
  .menu-section--beef { left: 50px; width: 507px; }
  .menu-section--seafood { left: 655px; width: 494px; }
  .section-title {
    margin: 0;
    text-align: center;
    color: var(--accent-red);
    font-weight: 400;
    font-size: 27px;
    letter-spacing: 0.5px;
    line-height: 32px;
  }
  .section-notes {
    margin: 14px 0 0;
    text-align: center;
    font-style: italic;
    font-weight: 300;
    font-size: 19.5px;
    line-height: 24.5px;
  }
  .dish-list {
    list-style: none;
    margin: 0;
    padding: 0;
  }
  .menu-section--beef .dish-list { margin-top: 24px; }
  .menu-section--seafood .dish-list { margin-top: 22px; }
  .dish-header {
    display: flex;
    justify-content: space-between;
    font-weight: 600;
    font-size: 18.5px;
    line-height: 24px;
    letter-spacing: 0.3px;
  }
  .dish-price { padding-right: 2px; }
  .dish-desc {
    margin: 0;
    text-align: right;
    font-style: italic;
    font-weight: 300;
    font-size: 18.5px;
    line-height: 23.5px;
    padding-bottom: 3px;
  }
  .dish-desc--featured { font-weight: 600; }
  .brand-mark {
    position: absolute;
    bottom: 36px;
    display: flex;
    align-items: center;
    gap: 5px;
    color: var(--accent-red);
    font-weight: 700;
    font-size: 12px;
    line-height: 1;
    letter-spacing: 0.3px;
  }
  .brand-mark::before {
    content: "";
    width: 10px;
    height: 10px;
    background: var(--accent-red);
  }
  .brand-mark--left { left: 22px; }
  .brand-mark--right { right: 16px; }
</style>
</head>
<body>
<main class="menu-page">
  <div class="backdrop-pattern" role="img" aria-label="Decorative geometric star-lattice pattern fading from gold at the top to red at the bottom"></div>
  <div class="column-divider"></div>

  <section class="menu-section menu-section--beef">
    <h2 class="section-title">BEEF &amp; PORK</h2>
    <p class="section-notes">Rice is not included. Add rice $1.25.<br>Enjoy a Half Chinese Chicken Salad or Plain Fried<br>Rice with any entrée for $5.50<br>Can replace Beef/Pork with Tofu for $1.50</p>
    <ul class="dish-list">
      <li class="dish"><div class="dish-header"><span class="dish-name">Mongolian Beef</span><span class="dish-price">12.25</span></div>
        <p class="dish-desc">Flank steak, garlic, ginger, and green onions on a<br>bed of white crunchies.</p></li>
      <li class="dish"><div class="dish-header"><span class="dish-name">Beef And Broccoli</span><span class="dish-price">11.95</span></div>
        <p class="dish-desc">Flank steak, broccoli, and black mushrooms sautéed<br>in a garlic brown sauce.</p></li>
      <li class="dish"><div class="dish-header"><span class="dish-name">Pepper Steak</span><span class="dish-price">11.95</span></div>
        <p class="dish-desc">Flank steak, bell peppers, onions, and garlic in black<br>pepper sauce.</p></li>
      <li class="dish"><div class="dish-header"><span class="dish-name">Sliced Barbequed Pork</span><span class="dish-price">8.95</span></div>
        <p class="dish-desc dish-desc--featured">Tender slices of juicy pork topped with scallions<br>in a barbeque sauce.</p></li>
      <li class="dish"><div class="dish-header"><span class="dish-name">Barbequed Spareribs</span><span class="dish-price">8.95</span></div>
        <p class="dish-desc">Slow-Roasted juicy pork ribs with barbeque sauce.</p></li>
      <li class="dish"><div class="dish-header"><span class="dish-name">Tangerine Beef</span><span class="dish-price">12.25</span></div>
        <p class="dish-desc">Crisp flank steak topped with scallions in a tangerine<br>sauce.</p></li>
      <li class="dish"><div class="dish-header"><span class="dish-name">Spicy Garlic Tomato Beef</span><span class="dish-price">12.95</span></div>
        <p class="dish-desc">Flank steak, tomato, water chestnuts, zucchini, onions,<br>and spicy garlic sauce.</p></li>
      <li class="dish"><div class="dish-header"><span class="dish-name">Ma Pao Tofu</span><span class="dish-price">7.95</span></div>
        <p class="dish-desc">Soft tofu cubes with ground pork or chicken cooked<br>in Szechuan-Style sauce.</p></li>
    </ul>
  </section>

  <section class="menu-section menu-section--seafood">
    <h2 class="section-title">SEAFOOD</h2>
    <p class="section-notes">Enjoy a Half Chinese Chicken Salad or Plain Fried<br>Rice with any entrée for $5.50<br>Can replace Seafood with Tofu for $1.50</p>
    <ul class="dish-list">
      <li class="dish"><div class="dish-header"><span class="dish-name">Crispy Spicy Honey Shrimp</span><span class="dish-price">13.95</span></div>
        <p class="dish-desc">Crispy large shrimp with red bell peppers, scallions,<br>and chili peppers in a sweet honey sauce.</p></li>
      <li class="dish"><div class="dish-header"><span class="dish-name">Kung Pao Three Treasures</span><span class="dish-price">13.95</span></div>
        <p class="dish-desc">Large shrimp, beef, and chicken breast with scal-<br>lions, peanuts, water chestnuts, and chili peppers.<br>Prepared mandarin-Style.</p></li>
      <li class="dish"><div class="dish-header"><span class="dish-name">Honey Walnut Shrimp</span><span class="dish-price">13.95</span></div>
        <p class="dish-desc">Lightly crisped savory shrimp with honey-Glazed<br>walnuts.</p></li>
      <li class="dish"><div class="dish-header"><span class="dish-name">Fish With Ginger Soy Sauce</span><span class="dish-price">15.95</span></div>
        <p class="dish-desc">Whole white fish filet steamed with ginger and<br>topped with green onions and cilantro.</p></li>
      <li class="dish"><div class="dish-header"><span class="dish-name">Shrimp With Snow Peas</span><span class="dish-price">13.95</span></div>
        <p class="dish-desc">Large shrimp with snow peas, water chestnuts,<br>carrots, and ginger in a white wine sauce.</p></li>
      <li class="dish"><div class="dish-header"><span class="dish-name">Shrimp With Lobster Sauce</span><span class="dish-price">13.95</span></div>
        <p class="dish-desc">Large shrimp, eggs, ground pork, snow peas, water<br>chestnuts, and red bell peppers sautéed in a lob-<br>ster sauce.</p></li>
      <li class="dish"><div class="dish-header"><span class="dish-name">Salt And Pepper Shrimp</span><span class="dish-price">13.95</span></div>
        <p class="dish-desc">Lightly battered large shrimp with a pepper spice;<br>served with bell peppers and white crunchies.</p></li>
      <li class="dish"><div class="dish-header"><span class="dish-name">Cashew Shrimp</span><span class="dish-price">13.95</span></div>
        <p class="dish-desc">Large shrimp with zucchini, onions, and roasted ca-<br>shews in oyster sauce.</p></li>
      <li class="dish"><div class="dish-header"><span class="dish-name">Orange Shrimp</span><span class="dish-price">13.95</span></div>
        <p class="dish-desc">Large crispy shrimp with onions and red and green<br>bell peppers in a sweet orange sauce.</p></li>
    </ul>
  </section>

  <div class="brand-mark brand-mark--left">Bao Lotus</div>
  <div class="brand-mark brand-mark--right">Bao Lotus</div>
</main>
</body>
</html>
```